Buisness card

**Front Side:**

**[Your Company Logo]**
**Steadfast Upkeep Engineering**
*Keeping Your Equipment Running Smoothly*

**Contact Information:**
- **Name:** [dale Harwick
- **Title:** [owner
- **Phone:** [5073918246
- **Email:** dale@suevx.com

**Back Side:**

**Services Offered:**
- Routine Inspections
- Equipment Maintenance
- Emergency Repairs
- Consultation Services
- New installs
Tag line
Be proactive not reactive

```html
<!DOCTYPE html>
<html lang="en">
<head>
<meta charset="utf-8">
<title>Steadfast Upkeep Engineering – Business Card</title>
<link rel="stylesheet" href="https://fonts.googleapis.com/css2?family=Roboto:wght@400;500;700&family=Montserrat:wght@700&family=Tinos&display=swap">
<style>
  :root {
    --bg: #1c1c1c;
    --card: #ffffff;
    --navy: #0c2f6e;
    --brand-blue: #0a3d8c;
    --name-blue: #0b3c78;
    --ink: #222222;
    --ink-soft: #333333;
    --accent-red: #e8333a;
    --band-light: #0b6b96;
    --band-mid: #0d3f80;
    --band-dark: #0a2a6c;
    --white: #ffffff;
  }
  * { margin: 0; padding: 0; box-sizing: border-box; }
  html, body { width: 1200px; height: 1059px; overflow: hidden; background: var(--bg); }
  body { position: relative; font-family: "Roboto", Arial, sans-serif; }

  .card {
    position: absolute;
    left: 254px;
    width: 698px;
    background: var(--card);
    border-radius: 24px;
    overflow: hidden;
  }
  .card--front { top: 97px; height: 397px; }
  .card--back  { top: 551px; height: 400px; width: 701px; }

  .brand {
    position: absolute;
    display: flex;
    align-items: center;
    gap: 22px;
  }
  .card--front .brand { left: 115px; top: 50px; }
  .card--back .brand  { left: 97px; top: 37px; }
  .brand__mark { width: 112px; height: 112px; border-radius: 50%; background: var(--navy); flex: none; }
  .brand__name {
    font-family: "Roboto", Arial, sans-serif;
    font-weight: 700;
    font-size: 36px;
    line-height: 1.1;
    color: var(--brand-blue);
    width: 340px;
  }

  .person { position: absolute; left: 45px; top: 195px; }
  .person__name { font-weight: 700; font-size: 27px; color: var(--name-blue); letter-spacing: -0.2px; }
  .person__title { font-family: "Tinos", "Times New Roman", serif; font-size: 17px; color: var(--ink); margin-top: 6px; }

  .divider { position: absolute; left: 44px; top: 271px; width: 610px; height: 1.5px; background: #3a3a3a; }

  .contact {
    position: absolute; top: 287px;
    display: flex; align-items: center; gap: 10px;
    font-size: 19px; color: var(--ink-soft); letter-spacing: 0.3px;
  }
  .contact--phone { left: 41px; }
  .contact--email { right: 42px; }
  .contact svg { flex: none; }

  .front-band {
    position: absolute; left: 0; right: 0; bottom: 0; height: 55px;
    border-top: 3px solid var(--accent-red);
    box-shadow: inset 0 3px 0 var(--white);
    background: radial-gradient(ellipse at 60% 0%, var(--band-light), var(--band-mid) 55%, var(--band-dark));
    display: flex; align-items: center; justify-content: center;
    padding-top: 4px;
  }
  .front-band__slogan { font-family: "Montserrat", Arial, sans-serif; font-weight: 700; font-size: 26px; color: var(--white); }

  .services {
    position: absolute; left: 0; right: 0; top: 177px; bottom: 0;
    background: radial-gradient(ellipse at 50% 0%, var(--band-light), var(--band-mid) 50%, var(--band-dark) 100%);
    color: var(--white); text-align: center;
  }
  .services__heading { font-weight: 500; font-size: 27px; margin-top: 24px; letter-spacing: 0.2px; }
  .services__list { list-style: none; font-size: 25px; line-height: 31px; margin-top: 11px; }
  .services__motto { font-weight: 700; font-size: 23px; margin-top: 13px; }
</style>
</head>
<body>

<section class="card card--front" aria-label="Business card front">
  <div class="brand">
    <div class="brand__mark"></div>
    <div class="brand__name">Steadfast Upkeep Engineering</div>
  </div>

  <div class="person">
    <div class="person__name">dale Harwick</div>
    <div class="person__title">Owner</div>
  </div>

  <div class="divider"></div>

  <div class="contact contact--phone">
    <svg width="20" height="20" viewBox="0 0 24 24" aria-hidden="true">
      <path fill="#0b3c78" d="M6.6 10.8a15.1 15.1 0 0 0 6.6 6.6l2.2-2.2a1 1 0 0 1 1-.25 11.4 11.4 0 0 0 3.6.57 1 1 0 0 1 1 1V20a1 1 0 0 1-1 1A17 17 0 0 1 3 4a1 1 0 0 1 1-1h3.5a1 1 0 0 1 1 1c0 1.25.2 2.45.57 3.57a1 1 0 0 1-.25 1z"/>
      <path fill="none" stroke="#0b3c78" stroke-width="1.8" d="M14 3.5a7 7 0 0 1 6.5 6.5M14 7a3.5 3.5 0 0 1 3 3"/>
    </svg>
    <span>5073918246</span>
  </div>

  <div class="contact contact--email">
    <svg width="20" height="15" viewBox="0 0 20 15" aria-hidden="true">
      <rect width="20" height="15" rx="1.5" fill="#0b3c78"/>
      <path d="M2 2l8 6 8-6" fill="none" stroke="#ffffff" stroke-width="1.8"/>
    </svg>
    <span>dale@suevx.com</span>
  </div>

  <div class="front-band">
    <span class="front-band__slogan">Keeping Your Equipment Running Smoothly</span>
  </div>
</section>

<section class="card card--back" aria-label="Business card back">
  <div class="brand">
    <div class="brand__mark"></div>
    <div class="brand__name">Steadfast Upkeep Engineering</div>
  </div>

  <div class="services">
    <h2 class="services__heading">SERVICES OFFERED</h2>
    <ul class="services__list">
      <li>• Routine Inspections • Equipment Maintenance</li>
      <li>• Emergency Repairs • Consultation Services</li>
      <li>• New installs</li>
    </ul>
    <p class="services__motto">Be proactive not reactive</p>
  </div>
</section>

</body>
</html>
```